Web Design for a recruitment company

Website is for a recruitment company, with a particular focus on temporary staff, trades, skilled, and unskilled labour markets. Website will consist of a home page design and separate design for additional pages. Website will be implemented as a template in SharePoint. There is a separate design project for a new logo and look colours will need to be co-ordinated.

Target Market(s)

Company executives in the construction and trades areas looking for staff. Trades people, skilled and unskilled labourers looking for work.

Industry/Entity Type

It Company

Number of Pages Required

2 page

Requirements
Must have
• Looking for Home Page design plus design for additional pages.
• .
Nice to have
• Right People | Right Place is the firms byline, company name is Voskin Staffing. They will be in the Logo (separate project) but may also appear elsewhere in the design.
• Company values (attached file) may be reflected in the design where practical.

```html
<!DOCTYPE html>
<html lang="en">
<head>
<meta charset="utf-8">
<title>Voskin Staffing – Right People | Right Place</title>
<link href="https://fonts.googleapis.com/css2?family=Open+Sans:wght@400;600;700&family=Oswald:wght@500&display=swap" rel="stylesheet">
<style>
:root{
  --navy:#0b2457;
  --navy-deep:#0a2150;
  --ink:#333333;
  --muted:#4a4a4a;
  --grey-band:#d3d3d3;
  --white:#ffffff;
  --black-band:#111111;
  --line:#bdbdbd;
}
*{margin:0;padding:0;box-sizing:border-box}
html,body{width:1200px;height:2311px;overflow:hidden}
body{font-family:"Open Sans",Arial,sans-serif;color:var(--ink);background:var(--white);position:relative}
section,header,footer,nav,article,div,a,p,h1,h2,h3,span{position:absolute}
a{color:inherit;text-decoration:none}

/* top bar */
.topbar{left:0;top:0;width:1200px;height:37px;background:var(--navy);color:var(--white);font-size:13px}
.topbar .contact{top:9px;display:flex;align-items:center;gap:10px}
.social{display:flex;gap:5px}
.social i{display:block;width:22px;height:22px;border-radius:50%;background:var(--white)}
.topbar .social{left:943px;top:7px}

/* header */
.site-header{left:0;top:37px;width:1200px;height:120px;background:var(--white)}
.brand{left:131px;top:24px;display:flex;align-items:center;gap:18px}
.brand-mark{position:relative;width:60px;height:60px;border-radius:50%;background:#6b6b6b}
.brand-text{position:relative}
.brand-name{position:relative;display:block;font-size:36px;font-weight:700;color:#222;line-height:1}
.brand-tag{position:relative;display:block;font-size:20px;color:#222;margin-top:6px}
.search{left:838px;top:26px;width:230px;height:23px;border:1px solid #ccc;background:#f4f4f4;font-size:8px;color:#999;padding:5px 8px}
.search svg{position:absolute;right:6px;top:5px}
.nav{left:645px;top:62px;display:flex;font-size:12.5px;color:var(--navy)}
.nav a{position:relative;padding:4px 17px;height:26px;line-height:18px;margin-right:6px}
.nav a.active{background:var(--navy);color:var(--white);padding:4px 16px}

/* hero */
.hero{left:0;top:157px;width:1200px;height:564px}
.hero-photo{left:0;top:0;width:1200px;height:564px;background:linear-gradient(180deg,#c9d2dc 0%,#aab6c2 45%,#5a6a85 100%)}
.hero-caption{left:0;top:441px;width:1200px;height:123px;background:rgba(40,48,60,.72)}
.hero-title{left:143px;top:18px;font-family:"Oswald",sans-serif;font-weight:500;font-size:36px;color:var(--white);letter-spacing:0}
.hero-sub{left:146px;top:77px;font-size:18px;color:var(--white)}
.hero-arrow{width:52px;height:52px;border-radius:50%;background:rgba(60,60,60,.8)}
.hero-arrow svg{position:absolute;left:16px;top:16px}

/* welcome */
.welcome{left:0;top:721px;width:1200px;height:189px;background:var(--grey-band);text-align:center}
.welcome h1{left:0;top:34px;width:1200px;font-size:23px;font-weight:400;color:#333;letter-spacing:.5px}
.welcome h1 b{color:var(--navy);font-weight:600;margin-left:8px}
.welcome p{left:205px;top:79px;width:790px;font-size:12.5px;line-height:27px;color:var(--muted)}

/* services */
.services{left:0;top:910px;width:1200px;height:347px;background:var(--white)}
.section-title{width:1200px;left:0;text-align:center;font-size:23px;font-weight:600;color:var(--navy)}
.services .section-title{top:22px}
.service{top:81px;width:230px;text-align:center}
.service .icon{position:relative;margin:0 auto;width:100px;height:100px;border-radius:50%;background:var(--navy)}
.service .icon svg{position:absolute;left:25px;top:25px}
.service h3{position:relative;margin-top:20px;font-size:13px;font-weight:400;color:#222}
.service p{position:relative;margin:8px auto 0;width:180px;font-size:12px;line-height:25px;color:var(--muted)}

/* values carousel */
.values{left:0;top:1257px;width:1200px;height:354px;background:var(--grey-band)}
.value{top:35px;width:223px}
.value h3{position:relative;font-size:13px;font-weight:700;color:var(--navy);margin-left:5px;height:41px}
.value-card{position:relative;width:223px;height:238px;background:var(--white);box-shadow:0 10px 12px -6px rgba(0,0,0,.35)}
.value-img{left:0;top:0;width:223px;height:174px}
.value-card p{left:21px;top:188px;font-size:12px;color:#333}
.value-card a{left:21px;top:209px;font-size:12px;font-weight:600;color:var(--navy)}

/* posts */
.posts{left:0;top:1611px;width:1200px;height:389px;background:var(--white)}
.posts .section-title{top:24px}
.post{top:67px;width:397px}
.post-img{position:relative;width:397px;height:174px}
.post p{position:relative;margin-top:16px;font-size:12.5px;line-height:26px;color:#333}
.post p a{position:static;color:var(--navy)}
.post hr{position:relative;display:block;border:0;border-top:1px solid var(--line);width:170px;margin-top:12px}
.post time{position:relative;display:block;font-size:12px;margin:14px 0 0 3px;color:#333}

/* footer */
.site-footer{left:0;top:2000px;width:1200px;height:246px;background:var(--navy-deep);color:var(--white)}
.foot-col{top:32px}
.foot-col h3{position:relative;font-size:15px;font-weight:400;margin-bottom:8px}
.foot-col a{position:relative;display:block;font-size:12px;line-height:24.5px}
.newsletter p{position:relative;width:210px;font-size:12px;line-height:19px;text-align:justify}
.newsletter .field{position:relative;width:208px;height:25px;background:var(--white);color:#aaa;font-size:11px;padding:5px 12px;margin-top:13px}
.newsletter .btn{position:relative;margin:14px 0 0 125px;width:85px;height:27px;background:#555;color:var(--white);font-size:12px;font-weight:600;text-align:center;line-height:27px}
.bottom-bar{left:0;top:2246px;width:1200px;height:65px;background:var(--black-band);color:var(--white)}
.bottom-bar p{left:126px;top:24px;font-size:12px}
.bottom-bar .social{left:914px;top:21px;gap:8px}
.bottom-bar .social i{width:26px;height:26px}
</style>
</head>
<body>

<div class="topbar">
  <div class="contact" style="left:134px">
    <svg width="14" height="10" viewBox="0 0 14 10"><rect x="0.5" y="0.5" width="13" height="9" fill="#fff"/><path d="M0.5 0.5 7 6 13.5 0.5" fill="none" stroke="#0b2457" stroke-width="1.2"/></svg>
    <span style="position:relative">info@voskinstaffing.com</span>
  </div>
  <div class="contact" style="left:404px">
    <svg width="12" height="12" viewBox="0 0 12 12"><path d="M2 0.5 4.5 3 3.3 4.6c.8 1.7 2.3 3.2 4.1 4.1L9 7.5 11.5 10 9.8 11.6C4.8 11 1 7.2.4 2.2Z" fill="#fff"/></svg>
    <span style="position:relative">(555) 014-2290</span>
  </div>
  <div class="social"><i></i><i></i><i></i><i></i><i></i></div>
</div>

<header class="site-header">
  <div class="brand">
    <span class="brand-mark"></span>
    <span class="brand-text">
      <span class="brand-name">Voskin Staffing</span>
      <span class="brand-tag">Right People | Right Place</span>
    </span>
  </div>
  <div class="search">Type search
    <svg width="10" height="10" viewBox="0 0 10 10"><circle cx="4" cy="4" r="3" fill="none" stroke="#999" stroke-width="1.2"/><path d="M6.2 6.2 9 9" stroke="#999" stroke-width="1.2"/></svg>
  </div>
  <nav class="nav">
    <a class="active" href="#">Home</a>
    <a href="#">About Us</a>
    <a href="#">Services</a>
    <a href="#">Careers</a>
    <a href="#">Contact Us</a>
  </nav>
</header>

<section class="hero">
  <div class="hero-photo" role="img" aria-label="Team of smiling business professionals in suits standing in a bright office"></div>
  <div class="hero-caption">
    <h2 class="hero-title">RIGHT PEOPLE | RIGHT PLACE</h2>
    <p class="hero-sub">Lorem Ipsum is simply text of the printing and typesetting industry. Lorem Ipsum has been the industry's .</p>
  </div>
  <div class="hero-arrow" style="left:50px;top:477px"><svg width="20" height="20" viewBox="0 0 20 20"><path d="M13 2 5 10l8 8" fill="none" stroke="#fff" stroke-width="2"/></svg></div>
  <div class="hero-arrow" style="left:1100px;top:477px"><svg width="20" height="20" viewBox="0 0 20 20"><path d="M7 2l8 8-8 8" fill="none" stroke="#fff" stroke-width="2"/></svg></div>
</section>

<section class="welcome">
  <h1>WELCOME TO <b>VOSKIN STAFFING</b></h1>
  <p>As the industry leaders in file management software systems for over a decade, Claimwise Online has been providing secure online claims software to a broad range of clients worldwide. The first part of providing any technical assistance to a company is to ensure that you understand what they do in their day to day business. It's a complete file management system.</p>
</section>

<section class="services">
  <h2 class="section-title">OUR SERVICES</h2>
  <div class="service" style="left:128px">
    <div class="icon"><svg width="50" height="50" viewBox="0 0 50 50" fill="#fff"><circle cx="16" cy="16" r="7"/><circle cx="34" cy="16" r="7"/><path d="M4 40c0-9 5-14 12-14s12 5 12 14Z"/><path d="M22 40c0-9 5-14 12-14s12 5 12 14Z"/></svg></div>
    <h3>TEMPORARY STAFF</h3>
    <p>Our management consulting services address our clienteles' crucial issues</p>
  </div>
  <div class="service" style="left:364px">
    <div class="icon"><svg width="50" height="50" viewBox="0 0 50 50" fill="#fff"><rect x="6" y="30" width="6" height="14"/><rect x="15" y="24" width="6" height="20"/><rect x="24" y="27" width="6" height="17"/><rect x="33" y="18" width="6" height="26"/><path d="M5 22 17 12l8 7 12-11" fill="none" stroke="#fff" stroke-width="3"/><path d="M33 5h9v9Z"/></svg></div>
    <h3>TRADES</h3>
    <p>Internal controls, including an organization's procedures and policies</p>
  </div>
  <div class="service" style="left:597px">
    <div class="icon"><svg width="50" height="50" viewBox="0 0 50 50" fill="#fff"><path d="M26 4c10 0 17 7 17 16 0 5-2 8-5 11v15H20v-7h-6c-2 0-3-1-3-3v-6l-4-2 4-6C11 12 17 4 26 4Z"/><circle cx="28" cy="18" r="7" fill="#0b2457"/></svg></div>
    <h3>SKILL LABOUR MARKETS</h3>
    <p>Our team of highly experienced and proficient legal team is ready to offer a range</p>
  </div>
  <div class="service" style="left:842px">
    <div class="icon"><svg width="50" height="50" viewBox="0 0 50 50" fill="#fff"><text x="19" y="16" font-family="Open Sans,sans-serif" font-size="17" font-weight="700">$</text><circle cx="11" cy="26" r="5"/><path d="M3 44c0-8 3-12 8-12s8 4 8 12Z"/><circle cx="39" cy="26" r="5"/><path d="M31 44c0-8 3-12 8-12s8 4 8 12Z"/><path d="M21 37h6v-3l4 4-4 4v-3h-6Z"/></svg></div>
    <h3>UNSKILLED LABOUR MARKETS</h3>
    <p>Investments are complex and intricate in nature, and for this they require</p>
  </div>
</section>

<section class="values">
  <div class="value" style="left:132px">
    <h3>ENJOY</h3>
    <div class="value-card">
      <div class="value-img" role="img" aria-label="Open hand holding a world map network with arrows" style="background:linear-gradient(160deg,#8a8a8a,#2e2e2e)"></div>
      <p>Etiam cursus leo</p><a href="#">MORE</a>
    </div>
  </div>
  <div class="value" style="left:368px">
    <h3>LOYALTY</h3>
    <div class="value-card">
      <div class="value-img" role="img" aria-label="Hand holding a cloud of colourful app icons" style="background:linear-gradient(160deg,#f4f4f4,#c9d6e6)"></div>
      <p>Etiam cursus leo</p><a href="#">MORE</a>
    </div>
  </div>
  <div class="value" style="left:605px">
    <h3>ENERGY</h3>
    <div class="value-card">
      <div class="value-img" role="img" aria-label="Light bulb containing a small green landscape on blue" style="background:linear-gradient(180deg,#3f9fd6,#0e5d95)"></div>
      <p>Etiam cursus leo</p><a href="#">MORE</a>
    </div>
  </div>
  <div class="value" style="left:843px">
    <h3>RELIABLE</h3>
    <div class="value-card">
      <div class="value-img" role="img" aria-label="Team working around a white desk with charts" style="background:linear-gradient(160deg,#e6e8ee,#b9bfcc)"></div>
      <p>Etiam cursus leo</p><a href="#">MORE</a>
    </div>
  </div>
  <svg style="position:absolute;left:62px;top:167px" width="26" height="34" viewBox="0 0 26 34"><path d="M20 2 6 17l14 15" fill="none" stroke="#9a9a9a" stroke-width="6"/></svg>
  <svg style="position:absolute;left:1114px;top:167px" width="26" height="34" viewBox="0 0 26 34"><path d="M6 2l14 15L6 32" fill="none" stroke="#9a9a9a" stroke-width="6"/></svg>
</section>

<section class="posts">
  <h2 class="section-title">LATEST POSTS</h2>
  <article class="post" style="left:188px">
    <div class="post-img" role="img" aria-label="Two colleagues reviewing documents at an office desk" style="background:linear-gradient(160deg,#d8d4cc,#5c5a58)"></div>
    <p>Lorem ipsum dolor sit amet, consectetur adipiscing elit. Quisque cursus, non turpis. Cras eu nibh dapibus justo fringilla.<a href="#">Read More..</a></p>
    <hr>
    <time>30 SEP 2014</time>
  </article>
  <article class="post" style="left:624px">
    <div class="post-img" role="img" aria-label="Business handshake on a light background" style="background:linear-gradient(90deg,#7d8796,#f2ebe0 55%,#d9ccb8)"></div>
    <p>Lorem ipsum dolor sit amet, consectetur adipiscing elit. Quisque cursus, non turpis. Cras eu nibh dapibus justo fringilla.<a href="#">Read More..</a></p>
    <hr>
    <time>30 SEP 2014</time>
  </article>
</section>

<footer class="site-footer">
  <div class="foot-col" style="left:134px">
    <h3>LINKS</h3>
    <a href="#">Home</a><a href="#">About Us</a><a href="#">Services</a><a href="#">Careers</a><a href="#">Contact Us</a>
  </div>
  <div class="foot-col" style="left:362px">
    <h3>COMPANY</h3>
    <a href="#">Press Room</a><a href="#">Careers</a><a href="#">Contact Us</a><a href="#">About Company</a><a href="#">Overview</a>
  </div>
  <div class="foot-col" style="left:599px">
    <h3>SUPPORT LINKS</h3>
    <a href="#">Help</a><a href="#">Terms &amp; Conditions</a><a href="#">Legal Notice</a><a href="#">Privacy Policy</a>
  </div>
  <div class="foot-col newsletter" style="left:858px">
    <h3>SIGN UP NEWSLETTER</h3>
    <p>Sign-up for our daily emails by entering your information below:</p>
    <div class="field">Name</div>
    <div class="field">Enter Your E-Mail ID</div>
    <div class="btn">Subscribe</div>
  </div>
</footer>

<div class="bottom-bar">
  <p>©2014 Voskin Staffing .All Rights Reserved</p>
  <div class="social"><i></i><i></i><i></i><i></i><i></i></div>
</div>

</body>
</html>
```